Flyer Ballettschule
Vielen Dank für den wirklich sehr professionellen superschönen Flyer. Uns hat das Design beim ersten Entwurf schon perfekt gefallen. Sofort hat der Designer kleine Änderungen bestens umgesetzt. Sehr netter Kontakt. Ein ganz großes Dankeschön! Ballettschule Wendelmoor

```html
<!DOCTYPE html>
<html lang="de">
<head>
<meta charset="utf-8">
<title>Flyer Ballettschule Wendelmoor</title>
<link rel="stylesheet" href="https://fonts.googleapis.com/css2?family=Noto+Serif:ital,wght@0,400;0,700;1,400&family=Alegreya+SC&family=Cormorant+Garamond:ital,wght@1,700&family=PT+Sans&display=swap">
<style>
:root{
  --red:#a3161d;
  --ink:#1a1a1a;
  --grey:#555;
  --light:#fff;
  --bg-top:#9a9a9a;
  --bg-bottom:#1a1a1a;
}
*{margin:0;padding:0;box-sizing:border-box}
html,body{width:1200px;height:1190px;overflow:hidden}
body{background:linear-gradient(var(--bg-top),var(--bg-bottom));position:relative;font-family:"Noto Serif",serif;color:var(--ink)}
.panel{position:absolute;top:53px;width:521px;height:1095px;background:var(--light);overflow:hidden}
.panel-left{left:56px}
.panel-right{left:613px}
.band{position:absolute;left:0;bottom:0;width:100%;height:16px;background:var(--red)}
.abs{position:absolute;z-index:2}
.quote{left:0;width:521px;top:42px;text-align:center;font-size:40px;font-weight:400;line-height:50px;color:var(--red)}
.quote-mark{display:inline-block;width:42px;height:42px;border-radius:50%;background:#ddd;color:var(--red);font-weight:700;font-size:38px;line-height:54px;text-align:center;vertical-align:middle}
.center{left:0;width:521px;text-align:center}
.intro{top:168px;font-size:17px;line-height:23px}
.lead{top:262px;font-size:17px;line-height:23px;color:var(--grey)}
.benefits{top:326px;list-style:none;font-size:17px;line-height:22px;color:var(--grey)}
.benefits li::before{content:"·  "}
.kids-note{top:486px;font-size:17px;line-height:23px}
.harmony{top:572px;font-size:17px;line-height:22px;font-style:italic;color:var(--red)}
.photo{position:absolute;z-index:1}
.photo-dancer{left:0;top:700px;width:300px;height:380px;background:radial-gradient(ellipse at 45% 50%,#c4c4c4,#e6e6e6 50%,#fff 72%)}
.photo-show{left:239px;top:662px;width:264px;height:174px;background:linear-gradient(135deg,#a2584a,#d47c96 50%,#6b5a4c)}
.photo-studio{left:239px;top:870px;width:264px;height:178px;background:linear-gradient(#d8d2c0,#b5a98a 55%,#8a5c2c)}
.photo-feet{left:150px;top:0;width:371px;height:110px;background:linear-gradient(#efefef,#fff)}
.mark-area{left:8px;top:30px;width:215px;height:190px;background:radial-gradient(ellipse,#f3d5d6,#fff 70%);z-index:1}
.welcome{left:0;right:0;top:98px;text-align:right;font-family:"Cormorant Garamond",serif;font-style:italic;font-weight:700;font-size:64px;line-height:52px;color:var(--red)}
.welcome span{display:block}
.welcome .w1{margin-right:34px}
.welcome .w2{margin-right:124px}
.welcome .w3{margin-right:137px}
.welcome .w4{margin-right:66px}
.invite{left:38px;top:338px;width:458px;text-align:center;font-family:"Alegreya SC",serif;font-size:21px;color:#555;border-bottom:3px solid var(--red);padding-bottom:4px}
.photo-couple{left:0;top:435px;width:310px;height:570px;background:radial-gradient(ellipse 45% 50% at 42% 50%,#ddd2ea,#ece8ef 55%,#fff 100%)}
.list{right:27px;text-align:right;font-size:17.5px;line-height:24.3px;color:var(--grey)}
.list h2{font-size:17.5px;font-weight:700;color:var(--ink);line-height:26px}
.list small{font-size:14px;line-height:18px;display:block}
.kids{top:389px}
.adults{top:575px}
.stars{right:27px;top:776px;color:var(--red);font-size:18px;letter-spacing:12px}
.contact{right:29px;text-align:right;font-family:"PT Sans",sans-serif;font-size:15.5px;line-height:24px;color:var(--red)}
.contact .label{color:var(--ink)}
.addr{top:821px}
.phones{top:928px}
.web{top:985px}
.member{left:0;width:521px;top:1044px;text-align:center;font-family:"Alegreya SC",serif;font-size:22px;color:#555}
</style>
</head>
<body>
<section class="panel panel-left">
  <h1 class="abs quote"><span class="quote-mark">“</span>Tanz ist Nahrung<br>für Gehirn und Seele.<span class="quote-mark">”</span></h1>
  <p class="abs center intro">Im Tanz bilden Körper und Geist eine Einheit.<br>Neue Bereiche im Gehirn werden erschlossen<br>und immer wieder trainiert und gestärkt.</p>
  <p class="abs center lead">Eine Grundausbildung im Klassischen<br>Ballett führt zu:</p>
  <ul class="abs center benefits">
    <li>gesunden Kräftigung der gesamten Muskulatur</li>
    <li>fördert eine gute Körperhaltung</li>
    <li>Erweiterte Wahrnehmungsfähigkeit</li>
    <li>Verbesserung des Konzentrationsvermögen</li>
    <li>Selbstwertgefühl wird verstärkt</li>
    <li>Disziplin, Respekt und Genauigkeit</li>
  </ul>
  <p class="abs center kids-note">Besonders für Kinder unterstützt Ballettunterricht<br>jegliche Bewegungsform und verhilft nachweislich<br>zu besseren Schulergebnissen.</p>
  <p class="abs center harmony">Tanzen, Kunst und Musik fördern in Ihrer Einheit die<br>emotionale Ausgeglichenheit und den Sinn<br>für Grazie und Harmonie.</p>
  <div class="photo photo-dancer" role="img" aria-label="Blasses Foto eines Tanzpaares in einer Hebefigur"></div>
  <div class="photo photo-show" role="img" aria-label="Foto einer Kinderaufführung mit Tutus vor einem Backsteingebäude"></div>
  <div class="photo photo-studio" role="img" aria-label="Foto des Ballettsaals mit Stange, Spiegeln und Holzboden"></div>
  <div class="band"></div>
</section>

<section class="panel panel-right">
  <div class="photo photo-feet" role="img" aria-label="Blasses Foto von Tänzerinnenbeinen an der Stange"></div>
  <div class="abs mark-area" role="img" aria-label="Springende Tänzerin als rote Silhouette"></div>
  <h1 class="abs welcome"><span class="w1">Willkommen</span><span class="w2">in der</span><span class="w3">Ballettschule</span><span class="w4">Wendelmoor!</span></h1>
  <p class="abs invite">Herzliche Einladung zu einer Probestunde!</p>
  <div class="photo photo-couple" role="img" aria-label="Foto eines Ballettpaares, Tänzerin im lila Tutu auf Spitze mit Partner in Schwarz"></div>
  <div class="abs list kids">
    <h2>KINDER UND JUGENDLICHE:</h2>
    <p>· Tänzerische Früherziehung ab 3 Jahren</p>
    <p>· Ballettvorbereitung ab 4 Jahren</p>
    <p>· Klassisches Ballett ab 6 Jahren</p>
    <p>· Klassisches Ballett mit Spitze ab 12 Jahren</p>
    <p>· Jazz Tanz · Step Tanz · Hip Hop</p>
    <p>· Berufsvorbereitung Tanz</p>
  </div>
  <div class="abs list adults">
    <h2>ERWACHSENE:</h2>
    <p>· Klassisches Ballett</p>
    <small>(auch für Anfänger<br>und Wiedereinsteiger)</small>
    <p>· Jazz Tanz &nbsp;· Step Tanz</p>
    <p>· Flamenco</p>
    <p style="line-height:20px">· Tänzerische<br>Gymnastik 50+, 70+</p>
  </div>
  <div class="abs stars">★★★★★</div>
  <p class="abs contact addr">Ballettschule Wendelmoor<br>Inh. Marlene Wendelmoor<br>Lindenhofer Straße 14<br>25999 Birkenau-Mitte</p>
  <p class="abs contact phones"><span class="label">Telefon:</span> 04100 - 5550123<br><span class="label">Mobil:</span> 0170 - 5550987</p>
  <p class="abs contact web">Email: info@ballettschule-wendelmoor.de<br>Web: www.ballettschule-wendelmoor.de</p>
  <p class="abs member">Mitglied im Netzwerk für Tanzpädagogik</p>
  <div class="band"></div>
</section>
</body>
</html>
```